Dental office post card

Dental office promotion to new community
POST CARD SIZE 6" x 11" EDDM
Phone numner 555 318 2761.

Target Market(s)

mainly adults and families

Font styles to use
Sans Serif

Colors

Designer to choose colors to be used in the design.

Requirements
Must have
• Office pictures please see attched
• Doctor's picture please see attached
• Modern simple design
• Not too many words
• OPEN EVENINGS, SATURDAYS AND SUNDAYS
• Emergency and walk-in welcome
• FINANCING AVAILABLE
• MOST PPO INSURANCES ACCEPTED
• CONVENIENT LOCATION AT THE CORNER OF LINDEN RD AND BUSINESS 47
• Phone number (555) 318 -2761 please do not put the number on the website.
Nice to have
• brightsmileclinic.example
• Dr. Mira Tessel
• Friendly local dentist to serve your dental needs
• Norwell School of dentistry
• Hollis College, BA, Molecular Cell Biology
• US Army veteran, captain, dental officer

```html
<!DOCTYPE html>
<html lang="en">
<head>
<meta charset="utf-8">
<title>Bright Smile Clinic – Postcard</title>
<link rel="stylesheet" href="https://fonts.googleapis.com/css2?family=Oswald:wght@300;400;600&family=Roboto:ital,wght@0,300;0,400;0,500;0,700;1,400&display=swap">
<style>
  :root{
    --teal:#2b8ca8;
    --teal-light:#4aa3bc;
    --charcoal:#4d4949;
    --ink:#555353;
    --paper:#ffffff;
    --backdrop:#b7b7b7;
    --line:#dcdcdc;
    --stamp:#eeeeee;
  }
  *{box-sizing:border-box;margin:0;padding:0}
  html,body{width:800px;height:1200px;overflow:hidden}
  body{background:var(--backdrop);font-family:"Roboto",Arial,sans-serif;position:relative}
  .card{position:absolute;left:53px;width:694px;height:386px;background:var(--paper);overflow:hidden;box-shadow:0 3px 8px rgba(0,0,0,.35)}
  .card-front{top:170px}
  .card-back{top:630px}
  .card svg.art{position:absolute;left:0;top:0}
  .abs{position:absolute}

  .brand{display:flex;align-items:center;gap:8px;color:var(--ink);font-family:"Roboto",Arial,sans-serif;font-weight:300;white-space:nowrap}
  .brand-dot{border:2px solid var(--ink);border-radius:50%}
  .front-brand{left:362px;top:24px;font-size:36px}
  .front-brand .brand-dot{width:60px;height:60px}

  .headline{left:374px;top:112px;font-family:"Oswald",sans-serif;line-height:1}
  .headline .lead{display:block;color:var(--teal);font-weight:600;font-size:36px;letter-spacing:.3px}
  .headline .lead small{font-size:22px}
  .headline .tail{display:block;color:var(--ink);font-weight:300;font-size:36px;margin-top:8px}

  .offer-box{left:373px;top:228px;width:283px;height:73px;border:1.5px solid var(--teal);border-top:none;text-align:center}
  .offer-box::before,.offer-box::after{content:"";position:absolute;top:0;width:20px;border-top:1.5px solid var(--teal)}
  .offer-box::before{left:0}.offer-box::after{right:0}
  .offer-tag{position:absolute;left:23px;top:-10px;width:237px;height:24px;background:var(--teal);color:#fff;font-weight:500;font-size:17px;line-height:24px;letter-spacing:.4px}
  .offer-hours{padding-top:21px;color:var(--ink);font-weight:500;font-size:17px;line-height:23px;letter-spacing:.3px}

  .book-tag{left:296px;top:341px;color:#fff;font-weight:500;font-size:13.5px;letter-spacing:.2px}
  .front-phone{left:484px;top:336px;color:#fff;font-weight:500;font-size:22px;display:flex;align-items:center;gap:8px}

  .benefit-tab{left:0;top:26px;width:142px;height:22px;background:#fff;border-radius:0 11px 11px 0;color:var(--ink);font-weight:700;font-size:12.5px;line-height:22px;padding-left:26px}
  .benefits{left:26px;top:58px;list-style:none;color:#fff;font-size:10.5px;line-height:15.5px}
  .benefits li,.creds li{display:flex;align-items:center;gap:5px}
  .tick{width:8px;height:8px;flex:none}

  .doc-title{left:25px;top:250px;color:#fff;font-weight:700;font-size:14px;letter-spacing:.3px}
  .doc-tagline{left:27px;top:274px;color:#fff;font-style:italic;font-size:8.5px;text-decoration:underline}
  .creds{left:27px;top:291px;list-style:none;color:#fff;font-size:8.5px;line-height:14px}
  .contact{left:27px;top:351px;color:#fff;font-weight:500;font-size:9.5px;display:flex;align-items:center;gap:5px}
  .contact-web{left:145px}

  .back-brand{left:393px;top:34px;font-size:24px;gap:6px}
  .back-brand .brand-dot{width:40px;height:40px;border-width:1.5px}
  .stamp-box{left:608px;top:24px;width:65px;height:65px;background:var(--stamp)}
  .address-line{left:438px;width:235px;height:1px;background:var(--line)}
</style>
</head>
<body>

<section class="card card-front" aria-label="Postcard front">
  <svg class="art" width="694" height="386" viewBox="0 0 694 386" aria-hidden="false">
    <defs>
      <linearGradient id="patientTone" x1="0" y1="0" x2="1" y2="1">
        <stop offset="0" stop-color="#dfe6ee"/>
        <stop offset=".45" stop-color="#c6a58f"/>
        <stop offset=".75" stop-color="#5f6f88"/>
        <stop offset="1" stop-color="#9fb9dc"/>
      </linearGradient>
      <clipPath id="photoCircle"><circle cx="120" cy="190" r="222"/></clipPath>
    </defs>
    <g clip-path="url(#photoCircle)">
      <rect x="0" y="0" width="400" height="400" fill="url(#patientTone)" role="img" aria-label="Photo of a smiling patient in a dental chair with a dentist holding instruments"/>
    </g>
    <path d="M255,-3 A236 236 0 0 1 348 251" fill="none" stroke="var(--teal)" stroke-width="5"/>
    <polygon points="246,386 288,326 694,326 694,386" fill="var(--charcoal)"/>
    <polygon points="300,337 465,337 457,363 292,363" fill="var(--teal)"/>
  </svg>

  <div class="abs brand front-brand"><span class="brand-dot"></span>BRIGHT SMILE</div>

  <h1 class="abs headline">
    <span class="lead">PATIENT COMFORT <small>IS</small></span>
    <span class="tail">OUR TOP PRIORITY</span>
  </h1>

  <div class="abs offer-box">
    <div class="offer-tag">FINANCING AVAILABLE</div>
    <p class="offer-hours">OPEN EVENINGS<br>SATURDAYS AND SUNDAYS</p>
  </div>

  <p class="abs book-tag">BOOK AN APPOITMENT</p>
  <p class="abs front-phone">
    <svg width="17" height="17" viewBox="0 0 24 24" aria-hidden="true"><path fill="#fff" d="M6.6 10.8a15.2 15.2 0 0 0 6.6 6.6l2.2-2.2a1 1 0 0 1 1-.25 11.4 11.4 0 0 0 3.6.57 1 1 0 0 1 1 1V20a1 1 0 0 1-1 1A17 17 0 0 1 3 4a1 1 0 0 1 1-1h3.5a1 1 0 0 1 1 1c0 1.25.2 2.45.57 3.57a1 1 0 0 1-.25 1z"/></svg>
    555 318 2761
  </p>
</section>

<section class="card card-back" aria-label="Postcard back">
  <svg class="art" width="694" height="386" viewBox="0 0 694 386">
    <defs>
      <clipPath id="tealArea"><rect x="0" y="0" width="694" height="241"/></clipPath>
      <linearGradient id="officeWarm" x1="0" y1="0" x2="1" y2="1"><stop offset="0" stop-color="#a7896c"/><stop offset="1" stop-color="#6b5644"/></linearGradient>
      <linearGradient id="officeRoom" x1="0" y1="0" x2="1" y2="1"><stop offset="0" stop-color="#b98f86"/><stop offset="1" stop-color="#4e4a55"/></linearGradient>
      <linearGradient id="officeHall" x1="0" y1="0" x2="1" y2="1"><stop offset="0" stop-color="#d9c3a6"/><stop offset="1" stop-color="#8c6a4c"/></linearGradient>
      <linearGradient id="doctorTone" x1="0" y1="0" x2="0" y2="1"><stop offset="0" stop-color="#c9a58a"/><stop offset=".35" stop-color="#3b4d68"/><stop offset="1" stop-color="#2a3850"/></linearGradient>
    </defs>
    <circle cx="-60" cy="300" r="455" fill="var(--teal)" clip-path="url(#tealArea)"/>
    <path d="M291,0 A468 468 0 0 1 404 212" fill="none" stroke="var(--charcoal)" stroke-width="4"/>
    <polygon points="0,241 398,241 412,256 404,386 0,386" fill="var(--charcoal)"/>
    <line x1="0" y1="340" x2="280" y2="340" stroke="#6a6666" stroke-width="1"/>

    <circle cx="63" cy="190" r="38" fill="url(#officeWarm)" stroke="#fff" stroke-width="2" role="img" aria-label="Photo of the clinic reception wall"/>
    <circle cx="160" cy="190" r="38" fill="url(#officeRoom)" stroke="#fff" stroke-width="2" role="img" aria-label="Photo of a treatment room"/>
    <circle cx="256" cy="190" r="38" fill="url(#officeHall)" stroke="#fff" stroke-width="2" role="img" aria-label="Photo of the clinic hallway"/>

    <path d="M282,386 L282,290 Q290,250 330,238 L330,215 Q338,185 355,185 Q372,185 380,215 L380,238 Q420,250 428,290 L428,386 Z" fill="url(#doctorTone)" role="img" aria-label="Photo of the dentist in navy scrubs"/>
  </svg>

  <div class="abs benefit-tab">OUR BENEFIT</div>
  <ul class="abs benefits">
    <li><svg class="tick" viewBox="0 0 10 10"><rect x=".5" y=".5" width="9" height="9" fill="none" stroke="#fff"/><path d="M2 5l2 2 4-5" fill="none" stroke="#fff" stroke-width="1.3"/></svg>Open Evenings, Saturdays And Sundays</li>
    <li><svg class="tick" viewBox="0 0 10 10"><rect x=".5" y=".5" width="9" height="9" fill="none" stroke="#fff"/><path d="M2 5l2 2 4-5" fill="none" stroke="#fff" stroke-width="1.3"/></svg>Emergency And Walk-in Welcome</li>
    <li><svg class="tick" viewBox="0 0 10 10"><rect x=".5" y=".5" width="9" height="9" fill="none" stroke="#fff"/><path d="M2 5l2 2 4-5" fill="none" stroke="#fff" stroke-width="1.3"/></svg>Financing Available</li>
    <li><svg class="tick" viewBox="0 0 10 10"><rect x=".5" y=".5" width="9" height="9" fill="none" stroke="#fff"/><path d="M2 5l2 2 4-5" fill="none" stroke="#fff" stroke-width="1.3"/></svg>Most Ppo Insurances Accepted</li>
    <li><svg class="tick" viewBox="0 0 10 10"><rect x=".5" y=".5" width="9" height="9" fill="none" stroke="#fff"/><path d="M2 5l2 2 4-5" fill="none" stroke="#fff" stroke-width="1.3"/></svg>Convenient Location At The Corner Of Linden Rd And Business 47</li>
  </ul>

  <h2 class="abs doc-title">MEET DR. MIRA TESSEL</h2>
  <p class="abs doc-tagline">Friendly local dentist to serve your dental needs</p>
  <ul class="abs creds">
    <li><svg class="tick" viewBox="0 0 10 10"><rect x=".5" y=".5" width="9" height="9" fill="none" stroke="#fff"/><path d="M2 5l2 2 4-5" fill="none" stroke="#fff" stroke-width="1.3"/></svg>Norwell School of dentistry</li>
    <li><svg class="tick" viewBox="0 0 10 10"><rect x=".5" y=".5" width="9" height="9" fill="none" stroke="#fff"/><path d="M2 5l2 2 4-5" fill="none" stroke="#fff" stroke-width="1.3"/></svg>Hollis College, BA, Molecular Cell Biology</li>
    <li><svg class="tick" viewBox="0 0 10 10"><rect x=".5" y=".5" width="9" height="9" fill="none" stroke="#fff"/><path d="M2 5l2 2 4-5" fill="none" stroke="#fff" stroke-width="1.3"/></svg>US Army veteran, captain, dental officer</li>
  </ul>

  <p class="abs contact">
    <svg width="8" height="12" viewBox="0 0 8 12" aria-hidden="true"><rect x=".6" y=".6" width="6.8" height="10.8" rx="1" fill="none" stroke="#fff" stroke-width="1.2"/><circle cx="4" cy="9.6" r=".7" fill="#fff"/></svg>
    (555) 318 -2761
  </p>
  <p class="abs contact contact-web">
    <svg width="12" height="12" viewBox="0 0 12 12" aria-hidden="true"><g fill="none" stroke="#fff" stroke-width="1"><circle cx="6" cy="6" r="5.2"/><ellipse cx="6" cy="6" rx="2.3" ry="5.2"/><path d="M.8 6h10.4M1.6 3.3h8.8M1.6 8.7h8.8"/></g></svg>
    brightsmileclinic.example
  </p>

  <div class="abs brand back-brand"><span class="brand-dot"></span>BRIGHT SMILE</div>
  <div class="abs stamp-box"></div>
  <div class="abs address-line" style="top:200px"></div>
  <div class="abs address-line" style="top:232px"></div>
  <div class="abs address-line" style="top:264px"></div>
  <div class="abs address-line" style="top:296px"></div>
</section>

</body>
</html>
```